Medical Practice needs a Letterhead Design

We need a clean, modern letterhead design for our stem cell medical practice.

Industry/Entity Type

Medical

```html
<!DOCTYPE html>
<html lang="en">
<head>
<meta charset="utf-8">
<title>VitaCore Medical Letterhead Specification</title>
<link href="https://fonts.googleapis.com/css2?family=Roboto:wght@400;500&display=swap" rel="stylesheet">
<style>
  :root {
    --ink: #000000;
    --brand-navy: #2b3d52;
    --muted: #6b6b6b;
    --paper: #ffffff;
    --paper-edge: #b4b4b4;
    --backdrop: #ffffff;
  }
  html, body {
    margin: 0;
    padding: 0;
    width: 1200px;
    height: 1200px;
    overflow: hidden;
    background: var(--backdrop);
    font-family: "Roboto", Arial, sans-serif;
  }
  .spec-sheet {
    position: absolute;
    left: 0;
    top: 0;
    width: 1240px;
    height: 1240px;
    transform: scale(0.9677);
    transform-origin: 0 0;
  }
  .page-shadow {
    position: absolute;
    left: 230px;
    top: 83px;
    width: 740px;
    height: 1040px;
    background: var(--paper-edge);
  }
  .page {
    position: absolute;
    left: 227px;
    top: 83px;
    width: 731px;
    height: 1037px;
    background: var(--paper);
    box-shadow: 0 0 2px rgba(0,0,0,0.15);
  }
  .brand-name {
    position: absolute;
    left: 314px;
    top: 176px;
    font-size: 21px;
    font-weight: 400;
    color: var(--brand-navy);
    letter-spacing: 0.2px;
    white-space: nowrap;
  }
  .sender-details {
    position: absolute;
    right: 369px;
    top: 172px;
    text-align: right;
    font-size: 6.6px;
    line-height: 9.5px;
    color: var(--ink);
    white-space: nowrap;
  }
  .sender-details .abn { color: var(--muted); }
  .text-area {
    position: absolute;
    left: 314px;
    top: 260px;
    width: 555px;
    height: 770px;
    border: 2px solid var(--ink);
    box-sizing: border-box;
  }
  .letter {
    position: absolute;
    left: 315px;
    top: 0;
    font-size: 12px;
    line-height: 14.7px;
    color: var(--ink);
    letter-spacing: 0.15px;
    white-space: nowrap;
  }
  .letter p { margin: 0; position: absolute; left: 0; }
  .letter-date { top: 257px; left: auto !important; right: -556px; text-align: right; }
  .recipient { top: 308px; }
  .salutation { top: 404px; }
  .body-one { top: 419px; }
  .body-two { top: 569px; }
  .body-three { top: 630px; }
  .sign-off { top: 844px; }
  .signatory { top: 911px; }
  .web-address {
    position: absolute;
    right: 369px;
    top: 1079px;
    font-size: 8px;
    color: var(--ink);
  }
  .annotations {
    position: absolute;
    left: 0;
    top: 0;
  }
  .annotations .rule { stroke: var(--ink); stroke-width: 2.5; fill: none; }
  .annotations .label {
    font-family: "Roboto", Arial, sans-serif;
    font-size: 17px;
    fill: var(--ink);
  }
</style>
</head>
<body>
<div class="spec-sheet">
  <div class="page-shadow"></div>
  <div class="page"></div>

  <div class="brand-name">VitaCore Medical</div>
  <div class="sender-details">
    14 Harbour Street, Bellerive TAS 7018<br>
    T (03) 6100 4200 F (03) 6100 4210<br>
    <span class="abn">ABN 987 654 321</span>
  </div>

  <div class="text-area"></div>

  <div class="letter">
    <p class="letter-date">20 January 2015</p>
    <p class="recipient">Jack Doe<br>Address Line One<br>Address Line Two 1234</p>
    <p class="salutation">Dear Mr Doe,</p>
    <p class="body-one">Rum de nostore, sed mosandit essin et facculparum in eos voluptatur? Optatur epelitaspic tem<br>reped qui ommolup tatquata susam fuga. Vel eturest, sam lam, tem. Nam et officip saecus sitate mo<br>verum eum eaturia vendel iusa pelleni minvellupta id mos ea conectia doluptatis a dolo moluptatur,<br>is explicium hicim et laborem porempora vellupi demporibusam acearum ut maxim aut aperspienet<br>quidelisquam si dipsant as experum qui dolo tem re, quamuscim fugia volumet volupta tinvelest eum,<br>occum accum unt dit re officto et, comnima sedicilit audigendus denderibero inullit voluptu mquosae<br>pedigen dendem nulparu ntiaepu disque conem accus reperem eum, sinvererovit eatem laces expl<br>que maximodis et acerfer untiatias ipsum fugit, santem nienimo dionsequas eicipieni te ex ex et ut re<br>porempos conse solo quis et atiorum faces duciis nos renima nis aut dolectatem nissum est eius.</p>
    <p class="body-two">Ectotatios quis mossunt ea doles is nonsequ amusanim fugiam es in endel in es doluptatur? Agnati<br>busa sequi dolupta quostioris resti aut re nit ex essimi, imus sam sum que explame voluptaquo dolum<br>re, sit officitempe coreprem. Nequodi cipiendit oditat.</p>
    <p class="body-three">Amus, uteturi taspis estorumqui sectibusame doles est a quatibusam cumquam fugit autae magni<br>hicid ut reiciam quam nonseque ne doluptur? Undeliquia se non pligeni mpores est hitis ant, quiscit<br>dento voluptis mollanis doluptas con peditam nonemquist velendit dio et labo. Itas endusci liquid que<br>venderias esecea susantur sus estem dissuntur, soluptas dis rem fugiae. Itaturibus et veritatur siminit<br>faccuptatem anduntota nonse od esse et fuga. Aceaqui bea del iusantibus, sed exceper speligent<br>volupta quiantibus nectur audis dolupta di voloreprovid que ni sum fugiandem facero tesenisque eum<br>ressinci quatureped estem. Tet pro comnimil int faccum si blatem qui sustionet lati re molupta tatissi<br>tioris dolupta turio. Nam harcius andanis exceperum, sit aut harchil ide rernatur? Quisquo voluptas<br>doluptas diamus vento consed et et omnimi, sinctotas aut la pore none vellibus animin re cust,<br>ipsaped ut qui ditatia con plaborp orepre se nonsedis dolesequiam volupta consectem reptatectur<br>adigenis est voleniet dusa dolupta quoditatur repudia dio vo.</p>
    <p class="sign-off">Yours Sincerely</p>
    <p class="signatory">Name Here</p>
  </div>

  <div class="web-address">www.vitacoremedical.com</div>

  <svg class="annotations" width="1240" height="1240" viewBox="0 0 1240 1240" aria-hidden="true">
    <g class="rule">
      <path d="M211 87V259M206 87H216M206 259H216"/>
      <path d="M211 1033V1118M206 1033H216M206 1118H216"/>
      <path d="M297 272V309M293 272H302M293 309H302"/>
      <path d="M297 349V405M293 349H302M293 405H302"/>
      <path d="M297 550V570M293 550H302M293 570H302"/>
      <path d="M297 612V632M293 612H302M293 632H302"/>
      <path d="M297 790V846M293 790H302M293 846H302"/>
      <path d="M297 857V912M293 857H302M293 912H302"/>
      <path d="M227 1139H313M227 1134V1144M313 1134V1144"/>
      <path d="M871 1139H957M871 1134V1144M957 1134V1144"/>
      <path d="M880 447H978M890 438L880 447L890 456"/>
    </g>
    <text class="label" x="132" y="180">50mm</text>
    <text class="label" x="132" y="1083">25mm</text>
    <text class="label" x="236" y="298">10mm</text>
    <text class="label" x="236" y="385">15mm</text>
    <text class="label" x="240" y="568">5mm</text>
    <text class="label" x="240" y="629">5mm</text>
    <text class="label" x="236" y="825">15mm</text>
    <text class="label" x="236" y="892">15mm</text>
    <text class="label" x="244" y="1168">25mm</text>
    <text class="label" x="888" y="1168">25mm</text>
    <text class="label" x="988" y="453">Text:  Roboto</text>
    <text class="label" x="988" y="475">10pt, 100% Black</text>
  </svg>
</div>
</body>
</html>
```